Ridgemont Business Card Redesign

Using the current logo/tagline lock-up and icon, redesign the Ridgemont business card to better show the tagline and improve the layout to give the card a more timely design and a classic, sophisticated look. See attached Project Brief for more detail.

```html
<!DOCTYPE html>
<html lang="en">
<head>
<meta charset="utf-8">
<title>Ridgemont Capital – Business Card</title>
<link rel="stylesheet" href="https://fonts.googleapis.com/css2?family=Tinos:wght@400&family=Montserrat:wght@300;400&display=swap">
<style>
  :root {
    --page-bg: #eff0f1;
    --card-bg: #f1f1f1;
    --brand-blue: #1f6fc0;
    --title-blue: #2a7bd0;
    --name-ink: #3a3a3a;
    --body-ink: #6a6a6a;
    --mark-light: #a9d0f0;
  }
  * { margin: 0; padding: 0; box-sizing: border-box; }
  html, body { width: 1200px; height: 1200px; overflow: hidden; background: var(--page-bg); }
  .card {
    position: absolute; left: 210px; top: 388px;
    width: 780px; height: 452px;
    background: var(--card-bg);
    overflow: hidden;
    font-family: "Montserrat", sans-serif;
  }
  .brand { position: absolute; left: 44px; top: 42px; display: flex; align-items: center; gap: 14px; }
  .brand-dot { width: 56px; height: 56px; border-radius: 50%; background: var(--brand-blue); flex: none; }
  .brand-name {
    font-family: "Tinos", serif; font-weight: 400; color: var(--brand-blue);
    font-size: 27px; letter-spacing: 1.5px; line-height: 1;
  }
  .holder { position: absolute; left: 42px; top: 152px; }
  .holder-name { font-family: "Tinos", serif; font-weight: 400; font-size: 30px; line-height: 1; color: var(--name-ink); letter-spacing: 0.3px; }
  .holder-title { margin-top: 10px; font-size: 19px; line-height: 23px; color: var(--title-blue); font-weight: 400; }
  .address { position: absolute; left: 42px; top: 252px; font-size: 19px; line-height: 26px; color: var(--body-ink); font-weight: 300; font-style: normal; }
  .contacts { position: absolute; left: 42px; top: 314px; list-style: none; font-size: 19px; color: var(--body-ink); font-weight: 300; }
  .contacts li { display: flex; align-items: center; gap: 5px; height: 26.5px; }
  .contacts svg { width: 14px; height: 14px; fill: var(--brand-blue); flex: none; }
  .decor {
    position: absolute; left: 452px; top: 14px; width: 300px; height: 424px; border-radius: 150px;
    background: linear-gradient(180deg, rgba(255,255,255,0.9) 0%, rgba(220,234,248,0.8) 45%, var(--mark-light) 100%);
    opacity: 0.7;
  }
</style>
</head>
<body>
  <main class="card">
    <div class="decor" role="img" aria-label="Large faint brand emblem in white-to-light-blue gradient"></div>

    <header class="brand">
      <span class="brand-dot"></span>
      <div class="brand-name">RIDGEMONT CAPITAL</div>
    </header>

    <section class="holder">
      <h1 class="holder-name">DANIEL R. HARGROVE</h1>
      <p class="holder-title">Principal &amp;<br>Cheif marketing Officer</p>
    </section>

    <address class="address">
      47 Linden Crest Avenue<br>
      Suite 210, Fairview, CT 06492
    </address>

    <ul class="contacts">
      <li><svg viewBox="0 0 24 24"><path d="M6.6 10.8a15.1 15.1 0 0 0 6.6 6.6l2.2-2.2c.3-.3.7-.4 1-.2 1.1.4 2.3.6 3.6.6.6 0 1 .4 1 1V20c0 .6-.4 1-1 1A17 17 0 0 1 3 4c0-.6.4-1 1-1h3.5c.6 0 1 .4 1 1 0 1.3.2 2.5.6 3.6.1.3 0 .7-.2 1z"/></svg>(555) 318-4720</li>
      <li><svg viewBox="0 0 24 24"><path d="M6.6 10.8a15.1 15.1 0 0 0 6.6 6.6l2.2-2.2c.3-.3.7-.4 1-.2 1.1.4 2.3.6 3.6.6.6 0 1 .4 1 1V20c0 .6-.4 1-1 1A17 17 0 0 1 3 4c0-.6.4-1 1-1h3.5c.6 0 1 .4 1 1 0 1.3.2 2.5.6 3.6.1.3 0 .7-.2 1z"/></svg>(555) 640-2283</li>
      <li><svg viewBox="0 0 24 24"><path d="M2 5h20v14H2z M2 5l10 8 10-8" fill="var(--brand-blue)" stroke="#fff" stroke-width="1.5"/></svg>dhargrove@ridgemontcapital.com</li>
      <li><svg viewBox="0 0 24 24"><circle cx="12" cy="12" r="10"/><path d="M2 12h20M12 2c3 3 3 17 0 20M12 2c-3 3-3 17 0 20M4 7h16M4 17h16" stroke="#fff" stroke-width="1.2" fill="none"/></svg>www.ridgemontcapital.com</li>
    </ul>
  </main>
</body>
</html>
```